Fahrzeugbeschriftung für Industriemaler-Unternehmen
Tolle Designer und sehr geduldig.
Zielgruppe
Wir sind Industriemaler Unternehmen und suchen ein hochwertiges und elegantes Design, unsere Zielgruppen sind allgemein in der Industrie Branche tätig, wie z. B. Medizinischer- und Technischer Gerätebau. Dazu gehören technische Kunststoffteile, Präzisionteile, Kleinmaschinen, Messgeräte, usw.
Aufgabenstellung
Das Design sollte präzis, elegant und Modern sein. Farbenkombination sollte mit Schwarzer Hintergrund sein, da unsere Fahrzeuge Schwarz sind. Wir sind in einem 2 sprachigen Standort tätig, daher sollte der design Deutsch und Französisch sein. Damit Sie einen besseren Überblick haben, können Sie gerne unsere Webseite anschauen. Als Bildmaterial haben wir nur unseren Logo.
Horizon Laque Atelier Sàrl
Birkenweg 14b
2563 Ipsach
info@laqueatelier-exemple.ch
www.laqueatelier-exemple.ch

```html
<!DOCTYPE html>
<html lang="de">
<head>
<meta charset="utf-8">
<title>Horizon Laque Atelier – Heckbeschriftung</title>
<link rel="stylesheet" href="https://fonts.googleapis.com/css2?family=Montserrat:wght@500;700&display=swap">
<style>
  :root {
    --page-bg: #e6e8ec;
    --door-bg: #2e2e2e;
    --door-edge: #1f1f1f;
    --window-line: #3c3c3c;
    --text: #ffffff;
    --paint-magenta: #c8449c;
    --paint-green: #7cc44a;
    --paint-blue: #3a8fd0;
    --paint-orange: #ee9a3a;
  }
  * { margin: 0; padding: 0; box-sizing: border-box; }
  html, body { width: 1200px; height: 800px; overflow: hidden; }
  body {
    background: var(--page-bg);
    font-family: "Montserrat", Arial, sans-serif;
    color: var(--text);
    position: relative;
  }
  .rear-artwork {
    position: absolute;
    left: 210px; top: 50px;
    width: 780px; height: 700px;
    display: flex; gap: 4px;
  }
  .door {
    position: relative;
    height: 100%;
    background: var(--door-bg);
    border: 2px solid var(--door-edge);
    border-radius: 14px;
    overflow: hidden;
  }
  .door--left { width: 470px; }
  .door--right { width: 306px; }
  .window-outline { position: absolute; inset: 0; pointer-events: none; }

  .service-list {
    position: absolute;
    left: 88px;
    list-style: none;
    font-weight: 700;
    font-size: 21px;
    line-height: 32px;
  }
  .service-list li::before {
    content: "";
    display: inline-block;
    width: 7px; height: 7px;
    border-radius: 50%;
    background: var(--text);
    margin: 0 16px 4px 0;
  }
  .service-list--de { top: 104px; }
  .service-list--fr { top: 232px; }

  .paint-area {
    position: absolute;
    left: 40px; right: 50px;
    top: 400px; bottom: 26px;
    border-radius: 36px;
    background: linear-gradient(115deg,
      var(--paint-magenta) 0%,
      var(--paint-green) 38%,
      var(--paint-blue) 68%,
      var(--paint-orange) 100%);
    opacity: 0.85;
  }

  .brand-mark {
    position: absolute;
    top: 112px; left: 50%;
    width: 80px; height: 80px;
    margin-left: -40px;
    border-radius: 50%;
    background: var(--text);
  }
  .brand-name {
    position: absolute;
    top: 232px; left: 0; right: 0;
    text-align: center;
    font-weight: 700;
    font-size: 26px;
    line-height: 32px;
  }

  .contact { position: absolute; left: 26px; }
  .social-links { top: 430px; display: flex; gap: 14px; }
  .social-links span {
    width: 32px; height: 32px;
    border: 3px solid var(--text);
    border-radius: 7px;
  }
  .web-contact {
    top: 486px;
    font-weight: 700;
    font-size: 16.5px;
    line-height: 34px;
  }
  .postal-address {
    top: 590px;
    font-style: normal;
    font-weight: 700;
    font-size: 13px;
    line-height: 19px;
  }
</style>
</head>
<body>
  <main class="rear-artwork">
    <section class="door door--left">
      <svg class="window-outline" viewBox="0 0 470 700" aria-hidden="true">
        <path d="M60 60 H450 V370 H50 Q30 370 32 345 L45 85 Q47 60 60 60 Z" fill="none" stroke="var(--window-line)" stroke-width="3"/>
      </svg>
      <ul class="service-list service-list--de" lang="de">
        <li>Einbrennlackierung</li>
        <li>Flüssige Lackierung</li>
        <li>Wiederaufrichtung</li>
      </ul>
      <ul class="service-list service-list--fr" lang="fr">
        <li>Thermolaquage</li>
        <li>Vernis liquide</li>
        <li>Remise en état</li>
      </ul>
      <div class="paint-area" role="img" aria-label="Illustration: bunte Farbspritzer in Magenta, Grün, Blau und Orange"></div>
    </section>

    <section class="door door--right">
      <svg class="window-outline" viewBox="0 0 306 700" aria-hidden="true">
        <path d="M20 60 H250 Q270 60 272 85 L285 345 Q287 370 262 370 H20 Z" fill="none" stroke="var(--window-line)" stroke-width="3"/>
      </svg>
      <div class="brand-mark" aria-hidden="true"></div>
      <h1 class="brand-name">Horizon Laque<br>Atelier</h1>

      <div class="contact social-links" aria-label="Soziale Netzwerke">
        <span></span><span></span>
      </div>
      <div class="contact web-contact">
        <p>info@laqueatelier-exemple.ch</p>
        <p>www.laqueatelier-exemple.ch</p>
      </div>
      <address class="contact postal-address">
        Horizon Laque Atelier Sàrl<br>
        Birkenweg 14b<br>
        2563 Ipsach
      </address>
    </section>
  </main>
</body>
</html>
```